Flyer-Design für regional agierendes Immobilienbüro
Zielgruppe
*regional agierendes Immobilienbüro
*Vermittlung von privaten Wohnimmobilien (Einfamilienhäuser, Wohnungen, Grundstücke)
*projektbezogene Zielgruppe: Immobilien Eigentümer / Verkäufer /Vermieter
*Idee: Gutschein über eine von drei Serviceleistungen - kostenlos*:
- Wertermittlung vom geprüften Preisbild-Berater
- Wohnflächen-Check
- Unterlagen-Check
*für Verkäufer / Vermieter im Wert von EUR 349,-
Aufgabenstellung
*CI (Style Guide, diverse Grafiken und Logos in verschiedenen Formaten vorhanden)
*cleanes, modernes Design - dennoch Eyecatcher (Postwurf)
*Ggf. DIN lang
Der Schlüssel zu einem erfolgreichen Verkauf liegt in der sorgfältigen Vorbereitung!
Passt der Verkaufspreis?
Sind alle Unterlagen vollständig und vorab auf mögliche 'Stolpersteine' geprüft?
Stimmt die Wohnfläche und sind alle Angaben rechtssicher korrekt?
Gerne prüfen wir, ob die grundlegenden Voraussetzungen für einen reibungslosen Verkauf Ihrer Immobilie zum bestmöglichen Verkaufspreis passen - kostenlos und unverbindlich! Im Rahmen eines unverbindlichen Beratungsgesprächs erfahren Sie auch, wie Sie von unserem vollumfänglichen Vermarktungsservice profitieren können.
Rufen Sie am besten gleich an und vereinbaren Sie einen Termin mit uns!

```html
<!DOCTYPE html>
<html lang="de">
<head>
<meta charset="utf-8">
<title>Gutschein-Flyer HOLLWEGER Immobilien</title>
<link href="https://fonts.googleapis.com/css2?family=Fira+Sans+Extra+Condensed:ital,wght@0,400;0,600;1,400;1,600;1,700&display=swap" rel="stylesheet">
<style>
  :root {
    --blue-dark: #0d4963;
    --blue-light: #33718d;
    --gold-light: #d9ac74;
    --gold-dark: #8c6a43;
    --white: #ffffff;
    --page: #ffffff;
    --photo-a: #3b4548;
    --photo-b: #c9ccc8;
  }
  * { margin: 0; padding: 0; box-sizing: border-box; }
  html, body { width: 849px; height: 1200px; overflow: hidden; background: var(--page); }
  body { position: relative; font-family: "Fira Sans Extra Condensed", "Arial Narrow", sans-serif; color: var(--white); }

  .flyer {
    position: absolute; left: 222px; top: 176px; width: 405px; height: 849px;
    box-shadow: 2px 3px 6px rgba(0,0,0,0.25);
  }
  .intro {
    position: absolute; left: 0; top: 0; width: 100%; height: 282px;
    background: linear-gradient(to bottom, var(--blue-dark), var(--blue-light));
    font-style: italic;
  }
  .intro p { position: absolute; left: 20px; right: 10px; font-size: 15.2px; line-height: 20.5px; letter-spacing: -0.25px; white-space: nowrap; }
  .intro p.wrap { white-space: normal; }
  .intro .question, .intro .cta { font-weight: 700; }

  .photo {
    position: absolute; left: 0; top: 284px; width: 100%; height: 321px;
    background: radial-gradient(ellipse at 55% 45%, var(--photo-b) 0%, #9aa0a0 40%, var(--photo-a) 100%);
  }

  .voucher {
    position: absolute; left: 0; top: 605px; width: 100%; height: 183px;
    background: linear-gradient(100deg, var(--gold-light), var(--gold-dark));
    font-style: italic;
    z-index: 2;
  }
  .cut-line { position: absolute; left: 0; width: 100%; height: 0; border-top: 1.5px dashed var(--white); }
  .cut-line.top { top: 0; }
  .cut-line.bottom { bottom: 0; }
  .scissors { position: absolute; width: 28px; height: 14px; z-index: 3; }
  .voucher-title { position: absolute; left: 20px; top: 34px; font-size: 31px; font-weight: 700; letter-spacing: -0.3px; }
  .service-list { position: absolute; left: 238px; top: 18px; list-style: none; font-size: 17.5px; font-weight: 600; line-height: 22px; text-transform: uppercase; }
  .divider { position: absolute; left: 20px; right: 20px; top: 95px; border-top: 1.5px solid rgba(255,255,255,0.85); }
  .voucher-text { position: absolute; left: 20px; right: 10px; top: 104px; font-size: 15.2px; font-weight: 700; line-height: 20px; letter-spacing: -0.25px; }
  .voucher-terms { position: absolute; left: 20px; top: 146px; font-size: 11.5px; }

  .contact {
    position: absolute; left: 0; top: 788px; width: 100%; height: 61px;
    background: linear-gradient(to bottom, var(--blue-light), var(--blue-dark));
    text-align: center; font-size: 12.5px; line-height: 17px; padding-top: 12px;
    white-space: nowrap;
  }
  .contact strong { font-weight: 600; }
  .sep { margin: 0 4px; }
</style>
</head>
<body>
  <div class="flyer">
    <section class="intro">
      <p style="top:24px">Können Sie diese 3 Fragen mit JA beantworten?</p>
      <p class="question" style="top:64px">- Passt der von Ihnen ermittelte Verkaufspreis?</p>
      <p class="question" style="top:105px">- Stimmt die Wohnfläche und sind alle Angaben rechtssicher?</p>
      <p class="question" style="top:146px">- Sind alle Unterlagen vollständig und auf Stolpersteine geprüft?</p>
      <p class="wrap" style="top:186px">Wir bieten mit unserem Gutschein Hilfestellung bei der Beantwortung dieser Fragen. Für Sie vollkommen unverbindlich und kostenlos!</p>
      <p class="cta" style="top:248px">Jetzt Gutschein einlösen und Sicherheit schaffen!</p>
    </section>

    <div class="photo" role="img" aria-label="Foto: Hände eines Beraters mit Kugelschreiber über einem Lageplan und Unterlagen auf dem Schreibtisch"></div>

    <section class="voucher">
      <div class="cut-line top"></div>
      <svg class="scissors" style="right:4px; top:-7px" viewBox="0 0 28 14" aria-hidden="true">
        <g fill="none" stroke="#fff" stroke-width="1.6">
          <circle cx="23" cy="3.5" r="2.6"/><circle cx="23" cy="10.5" r="2.6"/>
          <line x1="20.8" y1="4.8" x2="2" y2="10"/><line x1="20.8" y1="9.2" x2="2" y2="4"/>
        </g>
      </svg>
      <h2 class="voucher-title">GUTSCHEIN ÜBER:</h2>
      <ul class="service-list">
        <li>- Wertermittlung</li>
        <li>- Wohnflächen-Check</li>
        <li>- Unterlagen-Check</li>
      </ul>
      <div class="divider"></div>
      <p class="voucher-text">Mit diesem Gutschein erhalten Verkäufer / Vermieter eine der 3 oben genannten Serviceleistungen im Wert von 349 € kostenlos!</p>
      <p class="voucher-terms">Gültig bis 31.12.2018, keine Barauszahlung möglich.</p>
      <div class="cut-line bottom"></div>
      <svg class="scissors" style="left:4px; bottom:-7px" viewBox="0 0 28 14" aria-hidden="true">
        <g fill="none" stroke="#fff" stroke-width="1.6">
          <circle cx="5" cy="3.5" r="2.6"/><circle cx="5" cy="10.5" r="2.6"/>
          <line x1="7.2" y1="4.8" x2="26" y2="10"/><line x1="7.2" y1="9.2" x2="26" y2="4"/>
        </g>
      </svg>
    </section>

    <footer class="contact">
      <div>HOLLWEGER Immobilien<span class="sep">|</span>Jonas Brenner<span class="sep">|</span>Lindenweg 8<span class="sep">|</span>54321 Beispielstadt</div>
      <div><strong>Telefon: 09876 54 32 100</strong><span class="sep">|</span>www.hollweger-immo.de</div>
    </footer>
  </div>
</body>
</html>
```